Massage-Creme label for a young pharmacy

We are a young pharmacy which is part of a big union. We developed for a customer a very good massage creme with aloe vera, coconut oil, and many more advantages and as well a massage jelly. All we need is a good and affordable label which is beatiful and helps us to promote our product. As we want to develop further products, it would be very cool to have a corporate label for all upcoming products.

Target Market(s)

professional masseurs and physiotherapists

Industry/Entity Type

Health And Wellness

Font styles to use
Sans Serif
Decorative

Colors

Designer to choose colors to be used in the design.

Requirements
Must have
• Professionally looking design (but I'm sure you are doing so... :-)
Nice to have
• Label can have any shape. What you see is just a bad label with corresponding sizes, so you can imagine how it would look like in the final state.
Should not have
• If possible, the label should not be completely black (although it might look cool) as we are printing it on our own Vostek qr318-ux and black is difficult to print (and very costy).

```html
<!DOCTYPE html>
<html lang="de">
<head>
<meta charset="utf-8">
<title>Massage-créme Label</title>
<link rel="stylesheet" href="https://fonts.googleapis.com/css2?family=Fraunces:opsz,wght@72,700&family=Rubik:wght@400;700&display=swap">
<style>
  :root {
    --bg: #f5f6f5;
    --label: #ffffff;
    --salmon: #f4a07f;
    --mint: #68c5aa;
    --mint-text: #4fb996;
    --frame: #b9b9b9;
    --white: #ffffff;
  }
  * { margin: 0; padding: 0; box-sizing: border-box; }
  html, body {
    width: 1200px;
    height: 826px;
    overflow: hidden;
    background: var(--bg);
  }
  .label {
    position: absolute;
    left: 320px;
    top: 73px;
    width: 560px;
    height: 680px;
    background: var(--label);
  }
  .cut-line {
    position: absolute;
    inset: 30px 18px;
    border: 1.5px dashed var(--frame);
  }
  .product-name {
    position: absolute;
    top: 90px;
    width: 100%;
    text-align: center;
    font-family: "Fraunces", Georgia, serif;
    font-weight: 700;
    font-size: 51px;
    letter-spacing: 0.5px;
    color: var(--salmon);
  }
  .tagline {
    position: absolute;
    top: 209px;
    left: 50%;
    transform: translateX(-50%);
    padding: 0 3px 5px;
    border-bottom: 3px solid var(--salmon);
    font-family: "Rubik", Arial, sans-serif;
    font-size: 22px;
    color: var(--mint-text);
    white-space: nowrap;
  }
  .ingredient-band {
    position: absolute;
    left: 0;
    top: 0;
    width: 560px;
    height: 680px;
  }
  .ingredient {
    font-family: "Rubik", Arial, sans-serif;
    font-weight: 700;
    font-size: 23px;
    fill: var(--white);
  }
  .volume {
    position: absolute;
    top: 598px;
    width: 100%;
    display: flex;
    justify-content: center;
    align-items: center;
    gap: 22px;
    font-family: "Fraunces", Georgia, serif;
    font-weight: 700;
    font-size: 23px;
    color: var(--salmon);
  }
  .volume-rule {
    width: 82px;
    height: 3px;
    background: var(--salmon);
  }
</style>
</head>
<body>
  <div class="label">
    <div class="cut-line"></div>
    <h1 class="product-name">Massage-créme</h1>
    <p class="tagline">energetisch leitend</p>

    <svg class="ingredient-band" viewBox="0 0 560 680" xmlns="http://www.w3.org/2000/svg">
      <defs>
        <radialGradient id="ingredient-tones" cx="45%" cy="50%" r="60%">
          <stop offset="0%" stop-color="#efe6dc"/>
          <stop offset="55%" stop-color="#c08a68"/>
          <stop offset="100%" stop-color="#9fcfb0"/>
        </radialGradient>
      </defs>
      <rect x="0" y="365" width="560" height="35" fill="var(--mint)"/>
      <circle cx="280" cy="382" r="81" fill="var(--white)" stroke="var(--mint)" stroke-width="18"/>
      <g role="img" aria-label="Illustration of a halved coconut beside an aloe vera plant">
        <ellipse cx="280" cy="380" rx="58" ry="40" fill="url(#ingredient-tones)"/>
      </g>
      <text class="ingredient" x="110" y="391" text-anchor="middle">COCONUT</text>
      <text class="ingredient" x="440" y="391" text-anchor="middle">ALOE VERA</text>
    </svg>

    <div class="volume">
      <span class="volume-rule"></span>
      <span class="volume-text">℮ 1000 ml</span>
      <span class="volume-rule"></span>
    </div>
  </div>
</body>
</html>
```